Business Telephone Service Brochure

I need a brochure designed to help sell our VoIP service. The brochure needs to be clean, attention getting, professional and have 3 key areas of information (Key Features, Benefits & Service Plans). Here is an idea of what we are looking for https://www.artflockly.com/design/52930487. Need to also include how much the customer could save. See this for an example https://42mockups.com/postcard-flyer-design/contests/voip-sales-flyer-template-replicate-attached-358209. The Service Plan section needs to allow room for two types of plans. One plan includes the phone and has a 12, 24 and 36 month option. Each term (12,24,36) will have its own monthly cost per device. The second service option is no-commitment monthly with a single per month price per device. The included features section should allow for up to 16 features to be listed. The benefits should allow for 4-6 benefits to be listed. Also include room for Logo, business address, website, phone number and email.

Target Market(s)

Small to medium business with 1-100 employees.

Industry/Entity Type

Telecommunications

Font styles to use
Serif

Colors

Designer to choose colors to be used in the design.

Requirements
Must have
• Key Feature, Benefits and Service Plans (i.e. Pricing). Company logo, phone, email and website. Must have "Save up to x%!" and catch attention.
Nice to have
• Limited colors. I am not setting a hard limit, please take the liberty to do what you feel is needed. Just keep in mind we want it to be clean, professional and attention getting without being to flashy or obnoxious.
Should not have
• Nothing busy or distracting.

```html
<!DOCTYPE html>
<html lang="en">
<head>
<meta charset="utf-8">
<title>Corvane Business Phone Service Flyer</title>
<link href="https://fonts.googleapis.com/css2?family=Montserrat:wght@500;600;700&family=Source+Sans+3:wght@400;600&display=swap" rel="stylesheet">
<style>
:root{
  --navy:#1f2a72;
  --navy-deep:#141c4e;
  --orange:#f4a21c;
  --gold:#f6b93b;
  --paper:#f4f4f2;
  --ink:#1f2a72;
  --grey:#8c8f98;
  --steel:#c5cbd6;
  --backdrop:#4b4b53;
}
*{box-sizing:border-box;margin:0;padding:0}
html,body{width:1200px;height:800px;overflow:hidden}
body{background:var(--backdrop);font-family:"Source Sans 3",Arial,sans-serif;color:var(--ink)}
.flyer{position:absolute;left:330px;top:18px;width:540px;height:764px;background:var(--paper);overflow:hidden}

/* header */
.header{position:absolute;left:0;top:0;width:540px;height:160px}
.header-photo{position:absolute;right:0;top:0;width:400px;height:160px;background:linear-gradient(100deg,rgba(244,244,242,1) 0%,rgba(205,214,228,.7) 45%,rgba(228,233,240,.6) 100%)}
.header-wedge{position:absolute;left:0;top:0;width:230px;height:160px;background:linear-gradient(160deg,#8d9099,#6f727c);clip-path:polygon(0 0,55% 0,100% 100%,0 100%)}
.save{position:absolute;left:28px;top:56px;font-family:Montserrat,Arial,sans-serif;line-height:1}
.save-lead{font-size:24px;font-weight:500;color:#fff}
.save-amount{font-size:30px;font-weight:700;color:var(--gold);margin-top:4px}
.brand{position:absolute;right:30px;top:62px;text-align:right}
.brand-name{font-family:Montserrat,Arial,sans-serif;font-weight:700;font-size:44px;color:var(--navy);line-height:1;letter-spacing:-.5px}
.brand-tag{font-size:8px;color:var(--grey);margin-top:3px;letter-spacing:.2px}

/* key features */
.features{position:absolute;left:0;top:160px;width:540px;height:180px;background:linear-gradient(180deg,var(--navy) 0%,var(--navy-deep) 100%);border-top:4px solid var(--orange)}
.section-tab{position:absolute;background:var(--orange);color:var(--navy-deep);font-family:Montserrat,Arial,sans-serif;font-weight:700;font-size:15px;padding:4px 12px;letter-spacing:.3px}
.features .section-tab{left:220px;top:-18px}
.feature-cols{position:absolute;left:24px;top:34px;right:20px;display:flex}
.feature-col{list-style:none;flex:1;padding:0 12px;border-left:1px solid rgba(255,255,255,.35)}
.feature-col:first-child{border-left:none;padding-left:0}
.feature-col li{position:relative;padding-left:12px;color:#e6e8f2;font-size:10.5px;line-height:1.2;margin-bottom:8px}
.feature-col li::before{content:"✓";position:absolute;left:0;top:0;color:var(--gold);font-weight:600}

/* city strip */
.city-strip{position:absolute;left:0;top:340px;width:540px;height:70px;background:linear-gradient(90deg,#2b3668 0%,#7d8aa6 40%,#a9b4c6 70%,#5f6c8d 100%)}
.benefits-tab{left:18px;top:378px}

/* benefits */
.benefits{position:absolute;left:26px;top:410px;list-style:none}
.benefits li{position:relative;padding-left:14px;font-size:11px;line-height:1.45;color:var(--navy-deep)}
.benefits li::before{content:"";position:absolute;left:0;top:4px;width:7px;height:7px;border:1px solid var(--navy);border-radius:50%}
.phone-photo{position:absolute;right:20px;top:360px;width:210px;height:150px;border-radius:14px 14px 8px 8px;background:linear-gradient(150deg,#4a4d55 0%,#26282e 60%,#3a3d44 100%)}

/* plans */
.plans-title{position:absolute;left:0;right:0;top:528px;display:flex;align-items:center;gap:12px;padding:0 30px}
.plans-title .rule{flex:1;height:2px;background:var(--navy)}
.plans-title h2{font-family:Montserrat,Arial,sans-serif;font-size:17px;font-weight:700;color:var(--navy);letter-spacing:.3px}
.plans{position:absolute;left:22px;right:22px;top:556px;display:flex;justify-content:space-between}
.plan{position:relative;width:112px;height:112px}
.plan svg{position:absolute;inset:0}
.plan-body{position:absolute;inset:0;display:flex;flex-direction:column;align-items:center;justify-content:center;text-align:center;padding:0 16px}
.plan-price{font-family:Montserrat,Arial,sans-serif;font-weight:600;font-size:18px;color:var(--gold);line-height:1.1}
.plan-desc{font-size:9.5px;color:#fff;line-height:1.15;margin-top:3px}
.plan-desc small{display:block;font-size:7.5px}
.plan-term{font-size:9px;color:var(--gold);line-height:1.15;margin-top:3px}
.footnote{position:absolute;left:40px;right:40px;top:676px;font-size:8.5px;line-height:1.3;color:var(--navy-deep);text-align:center}

/* footer */
.footer{position:absolute;left:0;bottom:0;width:540px;height:46px;background:var(--navy);display:flex;align-items:center;gap:18px;padding-left:30px;color:#fff;font-size:11px}
.contact{display:flex;align-items:center;gap:6px}
.divider{width:1px;height:14px;background:rgba(255,255,255,.5)}
.footer-brand{position:absolute;right:0;bottom:0;width:130px;height:58px;background:var(--paper);display:flex;flex-direction:column;align-items:center;justify-content:center}
.footer-brand .brand-name{font-size:26px}
.footer-brand .brand-tag{font-size:5.5px}
</style>
</head>
<body>
<main class="flyer">
  <header class="header">
    <div class="header-photo" role="img" aria-label="Photo of glass office towers seen from below"></div>
    <div class="header-wedge"></div>
    <div class="save">
      <div class="save-lead">Save up to</div>
      <div class="save-amount">68% off</div>
    </div>
    <div class="brand">
      <div class="brand-name">Corvane</div>
      <div class="brand-tag">Internet·Telephone·Security·Networking</div>
    </div>
  </header>

  <section class="features">
    <h2 class="section-tab">KEY FEATURES</h2>
    <div class="feature-cols">
      <ul class="feature-col">
        <li>Unlimited local and long distance calling</li>
        <li>HD Voice</li>
        <li>Business SMS/Text Messaging</li>
        <li>Personal and Shared Voicemail Boxes</li>
        <li>Audio Conferencing</li>
      </ul>
      <ul class="feature-col">
        <li>Intercom</li>
        <li>Mobile App</li>
        <li>Auto Attendant/Interactive Voice Routing</li>
        <li>Free web or email fax</li>
      </ul>
      <ul class="feature-col">
        <li>Music On Hold - Customizable</li>
        <li>Simultaneous ring / follow-me</li>
        <li>Redundancy/Failover – Never miss a call</li>
        <li>Web admin portal</li>
      </ul>
    </div>
  </section>

  <div class="city-strip" role="img" aria-label="Photo of office building facades"></div>
  <div class="phone-photo" role="img" aria-label="Photo of a black desk IP phone with screen and keypad"></div>
  <h2 class="section-tab benefits-tab">BENEFITS</h2>
  <ul class="benefits">
    <li>No expensive onsite telephone equipment</li>
    <li>Easily scale up or down and needs change</li>
    <li>Free telephone/email support</li>
    <li>Lower monthly cost</li>
    <li>Increase reliability</li>
    <li>Easy self-administration</li>
  </ul>

  <div class="plans-title"><span class="rule"></span><h2>SERVICE PLANS</h2><span class="rule"></span></div>
  <div class="plans">
    <div class="plan">
      <svg viewBox="0 0 112 112"><polygon points="56,3 102,29.5 102,82.5 56,109 10,82.5 10,29.5" fill="#1f2a72" stroke="#f6b93b" stroke-width="3"/></svg>
      <div class="plan-body"><div class="plan-price">$21.95</div><div class="plan-desc">¹Phone service only<small>(phone sold separately)</small></div><div class="plan-term">No-commitment monthly</div></div>
    </div>
    <div class="plan">
      <svg viewBox="0 0 112 112"><polygon points="56,3 102,29.5 102,82.5 56,109 10,82.5 10,29.5" fill="#1f2a72" stroke="#f6b93b" stroke-width="3"/></svg>
      <div class="plan-body"><div class="plan-price">$24.95</div><div class="plan-desc">Service + ²Tellon T40 Phone</div><div class="plan-term">12 month term</div></div>
    </div>
    <div class="plan">
      <svg viewBox="0 0 112 112"><polygon points="56,3 102,29.5 102,82.5 56,109 10,82.5 10,29.5" fill="#1f2a72" stroke="#f6b93b" stroke-width="3"/></svg>
      <div class="plan-body"><div class="plan-price">$22.95</div><div class="plan-desc">Service + ²Tellon T40 Phone</div><div class="plan-term">24 month term</div></div>
    </div>
    <div class="plan">
      <svg viewBox="0 0 112 112"><polygon points="56,3 102,29.5 102,82.5 56,109 10,82.5 10,29.5" fill="#1f2a72" stroke="#f6b93b" stroke-width="3"/></svg>
      <div class="plan-body"><div class="plan-price">$20.95</div><div class="plan-desc">Service + ²Tellon T40 Phone</div><div class="plan-term">36 month term</div></div>
    </div>
  </div>
  <p class="footnote">¹For monthly service you may purchase the Tellon T40 phone for $65 each, less taxes and shipping.<br>²Tellon T40 phones are rented and due upon cancellation. Customer pays return shipping.</p>

  <footer class="footer">
    <span class="contact">
      <svg width="11" height="11" viewBox="0 0 24 24"><path fill="#fff" d="M6.6 10.8a15 15 0 0 0 6.6 6.6l2.2-2.2a1 1 0 0 1 1-.25 11.4 11.4 0 0 0 3.6.57 1 1 0 0 1 1 1V20a1 1 0 0 1-1 1A17 17 0 0 1 3 4a1 1 0 0 1 1-1h3.5a1 1 0 0 1 1 1c0 1.25.2 2.45.57 3.57a1 1 0 0 1-.25 1z"/></svg>
      (555) 014-2200</span>
    <span class="divider"></span>
    <span class="contact">
      <svg width="12" height="10" viewBox="0 0 24 18"><rect x="1" y="1" width="22" height="16" rx="2" fill="#fff"/><path d="M2 2l10 8 10-8" fill="none" stroke="#1f2a72" stroke-width="2"/></svg>
      hello@corvane.net</span>
    <span class="divider"></span>
    <span class="contact">
      <svg width="11" height="11" viewBox="0 0 24 24"><circle cx="12" cy="12" r="10" fill="none" stroke="#fff" stroke-width="2"/><path d="M2 12h20M12 2c3 3 3 17 0 20M12 2c-3 3-3 17 0 20" fill="none" stroke="#fff" stroke-width="1.6"/></svg>
      www.corvane.net</span>
    <div class="footer-brand">
      <div class="brand-name">Corvane</div>
      <div class="brand-tag">Internet·Telephone·Security·Networking</div>
    </div>
  </footer>
</main>
</body>
</html>
```